Pelloway Dental Care needs a functioning website with Wordpress

Our dental office needs a fully coded and functioning simple (3 page) website with Wordpress for us to be able to modify the content and add pages/tabs and be able to upload to Hostivo Linux hosting with cPanels for publication. The page should be professional, warm, inviting and easy to use and follow and content should be optimized for Zentrix search engine visibility. Please see the current temporary site for details of the office including contact info and mission: www.pellowaydentalcare.ca also see the attached files for logo and office photos.

Target Market(s)

Families

Industry/Entity Type

Dental Clinic

Coding

Coded - Design and coding required

Number of Pages Required

3 page

Font styles to use
Sans Serif

Requirements
Must have
• Wordpress coding, contact info, mission, photos, keywords and content for Zentrix search engine optimization, my logo, empty common tabs for us to be able to add content later such as services, hours, about us, etc.

```html
<!DOCTYPE html>
<html lang="en">
<head>
<meta charset="utf-8">
<title>Pelloway Dental Care</title>
<link href="https://fonts.googleapis.com/css2?family=Bree+Serif&family=Lato:wght@400;700&display=swap" rel="stylesheet">
<style>
:root{
  --green:#7dc243;
  --green-dark:#5f9e2a;
  --ink:#333333;
  --grey:#777777;
  --muted:#8a8a8a;
  --card:#6e6e6e;
  --footer:#494949;
  --footer-deep:#3a3a3a;
  --white:#ffffff;
}
*{margin:0;padding:0;box-sizing:border-box}
html,body{width:978px;height:1200px;overflow:hidden;background:var(--white)}
body{position:relative;font-family:'Lato',sans-serif;color:var(--ink)}
.abs{position:absolute}
.serif{font-family:'Bree Serif',serif}
.topline{left:0;top:0;width:978px;height:2px;background:#8a8a8a}
.brand{left:90px;top:26px;display:flex;align-items:center;gap:10px}
.brand-dot{width:34px;height:34px;border-radius:50%;background:var(--green)}
.brand-name{font-family:'Bree Serif',serif;font-size:27px;color:var(--green);letter-spacing:.5px}
.contact-top{top:17px;font-family:'Bree Serif',serif;font-size:13px;color:var(--grey);display:flex;align-items:center;gap:6px}
.nav{top:63px;left:418px;display:flex;font-family:'Bree Serif',serif;font-size:12px;color:var(--grey)}
.nav span{padding:0 15px;border-left:1px solid #aaa;line-height:14px}
.nav span:first-child{border:none;padding-left:6px;color:var(--green)}
.book{left:756px;top:54px;width:131px;height:25px;background:var(--green);color:#fff;font-family:'Bree Serif',serif;font-size:12px;display:flex;align-items:center;justify-content:center;border-radius:2px}
.hero-photo{left:0;top:112px;width:572px;height:364px;background:linear-gradient(135deg,#eae6e2 0%,#d9c7b6 40%,#c9b29c 70%,#e8e4e0 100%)}
.hero-text{right:91px;top:298px;width:330px;text-align:right;font-family:'Bree Serif',serif;font-size:20px;line-height:24.5px;color:#333}
.hero-arrows{left:839px;top:393px;display:flex;gap:5px}
.section-title{width:978px;left:0;text-align:center;font-family:'Bree Serif',serif}
.rule{height:1px;background:#bbb}
.welcome{top:508px;font-size:27px}
.welcome em{font-style:normal;color:var(--green)}
.lead{top:554px;width:978px;left:0;text-align:center;font-size:16.5px;color:#444}
.body{left:92px;top:583px;width:794px;text-align:center;font-size:12px;line-height:18.7px;color:var(--muted)}
.readmore{left:438px;top:655px;width:101px;height:27px;background:var(--green);border:1px solid var(--green-dark);border-radius:2px;color:#fff;font-family:'Bree Serif',serif;font-size:12px;display:flex;align-items:center;justify-content:center}
.services-bg{left:0;top:711px;width:978px;height:304px;background:linear-gradient(100deg,#b7bdc1 0%,#cfd2d3 35%,#c2b9b1 60%,#dcdcdc 80%,#b9bcbf 100%)}
.services-title{top:737px;font-size:26px;color:#fff}
.card{top:822px;width:168px;height:162px;background:var(--card);border:1px solid #555;color:#fff;text-align:center}
.card.active{background:var(--green);border-color:var(--green-dark)}
.card h3{font-family:'Bree Serif',serif;font-weight:400;font-size:21px;margin-top:47px;text-shadow:0 1px 2px rgba(0,0,0,.3)}
.card p{font-size:12px;line-height:14.5px;margin:8px 12px 0}
.card .notch{position:absolute;left:64px;bottom:-1px;width:40px;height:13px}
.icon{top:788px;width:72px;height:72px;border-radius:50%;background:#fff;border:4px solid #444;display:flex;align-items:center;justify-content:center}
.icon.active{border-color:var(--green-dark)}
.side{top:878px;width:26px;height:48px;background:#f2f2f2}
.footer{left:0;top:1015px;width:978px;height:145px;background:var(--footer);color:#fff}
.fnav{left:92px;top:1038px;font-size:11px;color:#fff;word-spacing:2px}
.fline{left:92px;top:1066px;width:585px;height:1px;background:#5d5d5d}
.fdiv{left:702px;top:1045px;width:1px;height:88px;background:#5d5d5d}
.fname{left:92px;top:1082px;font-size:14px;color:var(--green)}
.ftext{font-size:12px;color:#fff;line-height:18px}
.frow{display:flex;align-items:center;gap:8px;height:21.5px;font-size:11.5px}
.fbrand{left:722px;top:1060px;display:flex;align-items:center;gap:7px;font-family:'Bree Serif',serif;font-size:18px;color:#e6e6e6}
.fbrand-dot{width:22px;height:22px;border-radius:50%;background:#e6e6e6}
.social{top:1103px;width:23px;height:23px;border-radius:50%;background:var(--green)}
.bottom{left:0;top:1160px;width:978px;height:40px;background:var(--footer-deep)}
.copy{left:92px;top:1174px;font-size:11px;color:#ddd;letter-spacing:.3px}
.schedule{left:658px;top:1165px;width:226px;height:29px;background:var(--green);color:#fff;font-family:'Bree Serif',serif;font-size:15px;display:flex;align-items:center;gap:8px;padding-left:8px}
</style>
</head>
<body>
<div class="abs topline"></div>

<header>
  <div class="abs brand"><span class="brand-dot"></span><span class="brand-name">PELLOWAY DENTAL CARE</span></div>
  <div class="abs contact-top" style="left:580px">
    <svg width="8" height="13" viewBox="0 0 8 13"><path d="M2 0h2l1 3-1.5 1.2c.4 2 1.4 3.6 2.8 4.8L8 8l0 2.5-1.5 2C3 12 0 7 0 2z" fill="#7dc243"/></svg>
    905 555 0148
  </div>
  <div class="abs contact-top" style="left:692px;font-size:12px">
    <svg width="16" height="11" viewBox="0 0 16 11"><rect width="16" height="11" fill="#7dc243"/><path d="M0 0l8 6 8-6" stroke="#fff" fill="none"/></svg>
    hello@pellowaydentalcare.ca
  </div>
  <nav class="abs nav"><span>Home</span><span>About Us</span><span>Services</span><span>Contact Us</span></nav>
  <div class="abs book">Book An Appointment</div>
</header>

<section>
  <div class="abs hero-photo" role="img" aria-label="Smiling family of four: father, two children and mother"></div>
  <h1 class="abs hero-text" style="font-weight:400">We Are A Multidisciplinary Dental Practice Focusing On General And Specialist Dental Treatments</h1>
  <div class="abs hero-arrows">
    <svg width="20" height="20" viewBox="0 0 20 20"><circle cx="10" cy="10" r="9" fill="none" stroke="#7dc243" stroke-width="2"/><path d="M11.5 6l-4 4 4 4" fill="none" stroke="#7dc243" stroke-width="2"/></svg>
    <svg width="20" height="20" viewBox="0 0 20 20"><circle cx="10" cy="10" r="9" fill="none" stroke="#7dc243" stroke-width="2"/><path d="M8.5 6l4 4-4 4" fill="none" stroke="#7dc243" stroke-width="2"/></svg>
  </div>
</section>

<section>
  <div class="abs rule" style="left:115px;top:525px;width:133px"></div>
  <div class="abs rule" style="left:730px;top:525px;width:133px"></div>
  <h2 class="abs section-title welcome" style="font-weight:400">Welcome To The <em>Pelloway Dental Care</em></h2>
  <p class="abs lead">Duis autem vel eum iriure dolor in hendrerit in vulputate velit esse molestie consequat, velillum</p>
  <p class="abs body">Lorem ipsum dolor sit amet, consectetuer adipiscing elit, sed diam nonummy nibh euismod tincidunt ut laoreet dolore magna aliquam erat veolutpat. Ut wisi enim minim veniam, quis nostrud exerci tation ullamcorper suscipit lobortis nisl ut aliquip ex ea commodo consequat. Dolore eu feugiat nulla facilisis at vero eros et accumsan et iusto odio dignissim qui blandit praesent luptatum zzril delenit augue duis dolore te feugait nulla facilisi.</p>
  <div class="abs readmore">READ MORE</div>
</section>

<section>
  <div class="abs services-bg" role="img" aria-label="Soft-focus dental office backdrop with a large tooth model"></div>
  <div class="abs rule" style="left:274px;top:752px;width:124px;background:#eee"></div>
  <div class="abs rule" style="left:578px;top:752px;width:124px;background:#eee"></div>
  <h2 class="abs section-title services-title" style="font-weight:400">Our Services</h2>

  <div class="abs side" style="left:65px;border-radius:26px 0 0 26px;width:25px"></div>
  <svg class="abs" style="left:63px;top:893px" width="12" height="16" viewBox="0 0 12 16"><path d="M9 2L3 8l6 6" fill="none" stroke="#333" stroke-width="3"/></svg>
  <div class="abs side" style="left:888px;border-radius:0 26px 26px 0;width:25px"></div>
  <svg class="abs" style="left:902px;top:893px" width="12" height="16" viewBox="0 0 12 16"><path d="M3 2l6 6-6 6" fill="none" stroke="#333" stroke-width="3"/></svg>

  <div class="abs card active" style="left:119px"><h3>General</h3><p>Ut wisi enim ad mi erewnim veniam, quis nostrud exerc lobortis nislut commodo.</p><svg class="notch" viewBox="0 0 40 13"><path d="M0 13L14 0h12l14 13z" fill="#555"/><path d="M20 2v9M15.5 6.5h9" stroke="#fff" stroke-width="2"/></svg></div>
  <div class="abs card" style="left:309px"><h3>Cosmetic</h3><p>Ut wisi enim ad mi erewnim veniam, quis nostrud exerc lobortis nislut commodo.</p><svg class="notch" viewBox="0 0 40 13"><path d="M0 13L14 0h12l14 13z" fill="#444"/><path d="M20 2v9M15.5 6.5h9" stroke="#fff" stroke-width="2"/></svg></div>
  <div class="abs card" style="left:500px"><h3>Orthodontics</h3><p>Ut wisi enim ad mi erewnim veniam, quis nostrud exerc lobortis nislut commodo.</p><svg class="notch" viewBox="0 0 40 13"><path d="M0 13L14 0h12l14 13z" fill="#444"/><path d="M20 2v9M15.5 6.5h9" stroke="#fff" stroke-width="2"/></svg></div>
  <div class="abs card" style="left:690px"><h3>Implants</h3><p>Ut wisi enim ad mi erewnim veniam, quis nostrud exerc lobortis nislut commodo.</p><svg class="notch" viewBox="0 0 40 13"><path d="M0 13L14 0h12l14 13z" fill="#444"/><path d="M20 2v9M15.5 6.5h9" stroke="#fff" stroke-width="2"/></svg></div>

  <div class="abs icon active" style="left:167px"><svg width="40" height="32" viewBox="0 0 40 32"><circle cx="8" cy="6" r="4" fill="#222"/><path d="M4 12l10 10h20M18 22l-2 8M30 22l2 8" fill="none" stroke="#222" stroke-width="3"/></svg></div>
  <div class="abs icon" style="left:357px"><svg width="30" height="36" viewBox="0 0 30 36"><path d="M5 4c4-3 7 0 10 0s6-3 10 0c4 4 1 12 0 18-1 8-3 12-5 12s-2-8-5-8-3 8-5 8-4-4-5-12C4 16 1 8 5 4z" fill="none" stroke="#222" stroke-width="2.5"/></svg></div>
  <div class="abs icon" style="left:548px"><svg width="44" height="22" viewBox="0 0 44 22"><rect x="2" y="4" width="40" height="14" rx="4" fill="none" stroke="#222" stroke-width="3"/><path d="M2 11h40" stroke="#222" stroke-width="3"/><rect x="8" y="7" width="6" height="8" fill="#222"/><rect x="19" y="7" width="6" height="8" fill="#222"/><rect x="30" y="7" width="6" height="8" fill="#222"/></svg></div>
  <div class="abs icon" style="left:738px"><svg width="28" height="38" viewBox="0 0 28 38"><path d="M3 3c4-2 7 1 11 1s7-3 11-1c2 3 1 8-2 11H5C2 11 1 6 3 3z" fill="none" stroke="#222" stroke-width="2.5"/><path d="M9 17h10M10 21h8M10 25h8M11 29h6M12 33h4" stroke="#222" stroke-width="2.5"/></svg></div>
</section>

<footer>
  <div class="abs footer"></div>
  <div class="abs fnav">Home &nbsp;/&nbsp; About Us &nbsp;/&nbsp; Services &nbsp;/&nbsp; Contact Us</div>
  <div class="abs fline"></div>
  <div class="abs fdiv"></div>
  <div class="abs fname">Pelloway Dental Care</div>
  <div class="abs ftext" style="left:92px;top:1103px">12-40 Harrow Lane<br>Pelloway, ON L0A 1B2</div>
  <div class="abs ftext" style="left:298px;top:1079px">
    <div class="frow"><svg width="11" height="11" viewBox="0 0 11 11"><path d="M2 0h2l1 3-1.5 1c.6 1.5 1.6 2.5 3 3L7.5 6 11 7v2l-2 2C4 10 0 6 0 2z" fill="#fff"/></svg>905 555 0148</div>
    <div class="frow"><svg width="11" height="11" viewBox="0 0 11 11"><rect x="2" y="0" width="7" height="3" fill="#fff"/><rect x="0" y="3" width="11" height="5" fill="#fff"/><rect x="2" y="7" width="7" height="4" fill="#fff" stroke="#494949"/></svg>905 555 0149</div>
    <div class="frow"><svg width="11" height="8" viewBox="0 0 11 8"><rect width="11" height="8" fill="#fff"/><path d="M0 0l5.5 4L11 0" stroke="#494949" fill="none"/></svg>reception@pellowaydentalcare.ca</div>
  </div>
  <div class="abs ftext" style="left:520px;top:1077px;font-size:11.5px;line-height:21.5px"><b>Working Hours:</b><br>Monday to Friday 8am to 7pm<br>Sat: 9am to 2pm</div>
  <div class="abs fbrand"><span class="fbrand-dot"></span>PELLOWAY</div>
  <div class="abs social" style="left:761px"></div>
  <div class="abs social" style="left:790px"></div>
  <div class="abs social" style="left:819px"></div>
  <div class="abs bottom"></div>
  <div class="abs copy">©2016 Pelloway Dental Care. All Rights Reserved</div>
  <div class="abs schedule">
    <svg width="24" height="22" viewBox="0 0 24 22"><rect x="1" y="3" width="18" height="16" fill="none" stroke="#fff" stroke-width="2"/><path d="M1 8h18M6 1v4M14 1v4" stroke="#fff" stroke-width="2"/><circle cx="18" cy="16" r="5" fill="#7dc243" stroke="#fff" stroke-width="1.5"/><path d="M18 13v3h2" stroke="#fff" stroke-width="1.5" fill="none"/></svg>
    Schedule &amp; Appointment
  </div>
</footer>
</body>
</html>
```